"The Craft of Patron Care," fourth edition cover design

Later this year, my publisher, Harold Penmarsh & Daughters, will issue a fourth, substantially revised edition of "The Craft of Patron Care," following the 2016 publication of the third edition and the second and first versions that were issued earlier.

To distinguish this new edition from previous ones, I need a cover design that visually connects and is consistent with what has preceded it, while signaling this is a new and different, worthy of prospective readers/buyers’ attention.

Attached are three different verbal approaches to the new cover; these are NOT MEANT to serve as actual designs, but rather will give you a sense of how language is to be deployed:

The first emphasizes “ART” as the key visual word in the book title;
The second emphasizes “CLIENT SERVICE” as the key visual words in the book title; and,
The third emphasizes just the word "CLIENT" in the book title.

A top-of-the-page is a pre-head that applies to all three versions:
“6 TIMELESS PRINCIPLES FOR ADVERTISING & MARKETING PRO’s
IN AN AI WORLD"

There's a mid-page sub-head for all three versions:
“THE CLASSIC GUIDE,” followed by
“FOURTH EDITION BY GERALD ASHCOMBE

And there's a one-line, bottom-of-the-page designation:
“Foreword by Mae Dunford, Global Executive Creative Director, Starbolt"

The pallette for the previously published third edition was black with red as an accent color on a field of white; I've attached a sample for reference, so you can see how it was executed. For this new fourth edition, I'd like to change the accent color from red to either Wedgewood blue, or British racing green, or an alternative that is assertive and color saturated -- think of primary colors -- that contrast sufficiently with the base of black. As an alternative, you can consider a cover that used either Wedgewood blue, British racing green, or another possibility as a full-bleed field, with copy content either revered out or surprinted.

Lastly, while the new cover largely is meant to be typographically driven, if you can come up with a visual metaphor that illustrates and builds on the book's title, that would be very helpful. By way of reference, the third edition's book cover attempted to do this by introducing a visual element at the end of the book's title that's meant to represent an artist's paint splatter (although I admit it didn't work as well as it should).

Target Market(s)

Prospective purchasers of the book who might discover copies at a bookstore, but more likely will encounter it through online distributors such as Riverdex, Hartwell & Pike, and Tindall’s.

Industry/Entity Type

Advertising and marketing

Font styles to use
Serif
Sans Serif
Other font styles liked:
• A mix of serif and san-serif typefaces is okay. for the examples I shared, I relieid on "Arial Rounded Bold" but you need not be weeded to this. If you opt to mix in a serif font, I am partial to Cambria as a typeface.

Requirements
Must have
• To achieve the goal of being “connected with but distinct” from previous editions, the new cover should be:  Largely typographic, but displaying a color palette different from the previous editions’ black-plus-red-accent on a canvas of white.  Any new accent color selected for use should be vibrant, strong, and highly saturated; think “British racing green,” “Wedgewood blue,” or their equivalents.  In addition to a powerful, “billboard” approach to type and color, consider other visual metaphors that are likely to engage the readers. The winning cover design will stand out from other books, while connecting with the previously published third edition.
Nice to have
• If you can find way to illustrate the book's title through a visual metaphor, that would be ideal.a
Should not have
• Anything that is frivolous or non-sensical

```html
<!DOCTYPE html>
<html lang="en">
<head>
<meta charset="utf-8">
<title>The Craft of Patron Care — Fourth Edition Cover</title>
<link rel="stylesheet" href="https://fonts.googleapis.com/css2?family=Old+Standard+TT:wght@400;700&family=Rokkitt:wght@400;500&display=swap">
<style>
  :root {
    --racing-green: #00412a;
    --wedgwood: #8ea6dc;
    --paper: #ffffff;
    --backdrop: #f1f1ef;
    --label-ink: #0e3d2a;
  }
  * { box-sizing: border-box; margin: 0; padding: 0; }
  html, body {
    width: 1200px;
    height: 1200px;
    overflow: hidden;
    background: var(--backdrop);
  }
  .canvas {
    position: relative;
    width: 1200px;
    height: 1200px;
  }
  .cover {
    position: absolute;
    left: 200px;
    top: 30px;
    width: 800px;
    height: 1140px;
    background: var(--paper);
    box-shadow: 0 2px 14px rgba(0,0,0,0.12);
  }
  .field {
    position: absolute;
    left: 50px;
    top: 50px;
    width: 700px;
    height: 980px;
    background: var(--racing-green);
    display: flex;
    flex-direction: column;
    align-items: center;
    text-align: center;
  }
  .pre-head {
    margin-top: 80px;
    font-family: "Old Standard TT", serif;
    font-variant: small-caps;
    font-size: 27px;
    line-height: 1.25;
    letter-spacing: 1.5px;
    color: var(--wedgwood);
  }
  .title {
    margin-top: 130px;
    font-family: "Rokkitt", serif;
    font-weight: 400;
    line-height: 0.86;
  }
  .title-lead {
    display: block;
    color: var(--wedgwood);
    font-size: 66px;
    letter-spacing: -1px;
  }
  .title-lead .key-word {
    font-size: 118px;
    font-weight: 500;
  }
  .title-main {
    display: block;
    color: var(--paper);
    font-size: 168px;
    font-weight: 500;
    letter-spacing: -3px;
  }
  .edition {
    margin-top: 62px;
    font-family: "Old Standard TT", serif;
    color: var(--wedgwood);
    line-height: 1.2;
  }
  .edition-tag {
    display: block;
    font-variant: small-caps;
    font-size: 30px;
    letter-spacing: 2px;
  }
  .edition-number {
    display: block;
    font-weight: 700;
    font-size: 36px;
    letter-spacing: 2px;
  }
  .byline {
    position: absolute;
    left: 50%;
    top: 955px;
    transform: translateX(-50%);
    width: 400px;
    padding: 14px 18px 16px;
    background: var(--paper);
    border: 1px solid var(--label-ink);
    outline: 5px solid var(--paper);
    text-align: center;
    font-family: "Old Standard TT", serif;
    color: var(--label-ink);
  }
  .byline-author {
    font-size: 25px;
    letter-spacing: 1.5px;
    margin-bottom: 6px;
  }
  .byline-foreword {
    font-variant: small-caps;
    font-size: 19px;
    line-height: 1.3;
    letter-spacing: 0.5px;
  }
</style>
</head>
<body>
  <main class="canvas">
    <section class="cover" aria-label="Book cover: The Craft of Patron Care, fourth edition">
      <div class="field">
        <p class="pre-head">6 Timeless Principles for Advertising<br>&amp; Marketing Pros in an AI World</p>
        <h1 class="title">
          <span class="title-lead">The <span class="key-word">CRAFT</span> of</span>
          <span class="title-main">PATRON</span>
          <span class="title-main">CARE</span>
        </h1>
        <p class="edition">
          <span class="edition-tag">The Classic Guide</span>
          <span class="edition-number">FOURTH EDITION</span>
        </p>
      </div>
      <div class="byline">
        <p class="byline-author">GERALD ASHCOMBE</p>
        <p class="byline-foreword">Foreword by Mae Dunford,<br>Global Executive Creative Director,<br>Starbolt</p>
      </div>
    </section>
  </main>
</body>
</html>
```